RWL Business Cards

We need to design new business cards for our company. We are a Managed Discretionary Account (MDA) adviser based in Sydney Australia. We have distinct corporate colour pallet which will be provided and various logo formats. I will also include our current business card design as a guide only to what we have accepted previously. The final design should convey financial professionalism and experience as well as the necessary company information.

Target Market(s)

High Net Worth and Professional Investors

Industry/Entity Type

Financial

Font styles to use
Serif

```html
<!DOCTYPE html>
<html lang="en">
<head>
<meta charset="utf-8">
<title>RWL Capital Business Card</title>
<link rel="stylesheet" href="https://fonts.googleapis.com/css2?family=Open+Sans:wght@400;600;700&display=swap">
<style>
  :root {
    --page: #e4e5e7;
    --card-light: #fbfbfb;
    --card-shade: #e6e7e9;
    --charcoal: #2a2a2c;
    --green: #0f6a3c;
    --ink: #333336;
    --white: #ffffff;
  }
  * { margin: 0; padding: 0; box-sizing: border-box; }
  html, body {
    width: 1200px; height: 816px; overflow: hidden;
    background: var(--page);
    font-family: "Open Sans", Arial, sans-serif;
  }
  .card {
    position: absolute; left: 40px; top: 88px;
    width: 1120px; height: 640px;
    border-radius: 40px; overflow: hidden;
    box-shadow: 0 10px 30px rgba(0,0,0,0.18);
  }
  .card-shapes { position: absolute; inset: 0; }
  .holder { position: absolute; left: 64px; top: 208px; color: var(--ink); }
  .holder-name { font-size: 36px; font-weight: 700; letter-spacing: 0.5px; }
  .holder-role { font-size: 28px; color: var(--green); margin-top: 2px; }
  .contacts { position: absolute; left: 64px; top: 372px; list-style: none; color: var(--ink); }
  .contacts li { display: flex; align-items: flex-start; font-size: 25px; line-height: 35px; }
  .contacts .address { font-weight: 700; font-size: 24px; }
  .contacts svg { width: 22px; height: 22px; margin: 7px 14px 0 0; flex: none; fill: var(--green); }
  .brand-name {
    position: absolute; right: 80px; top: 300px;
    font-size: 66px; font-weight: 700; color: var(--green);
    letter-spacing: 1px;
  }
  .website {
    position: absolute; left: 710px; top: 448px; width: 410px;
    font-size: 33px; color: var(--white); text-align: center;
  }
</style>
</head>
<body>
  <div class="card">
    <svg class="card-shapes" width="1120" height="640" viewBox="0 0 1120 640">
      <defs>
        <linearGradient id="paper" x1="0" y1="0" x2="1" y2="1">
          <stop offset="0" stop-color="var(--card-shade)"/>
          <stop offset="0.45" stop-color="var(--card-light)"/>
          <stop offset="1" stop-color="var(--card-shade)"/>
        </linearGradient>
      </defs>
      <rect class="base-band" width="1120" height="640" fill="var(--charcoal)"/>
      <path class="paper-face" d="M0 0 H1120 V430 H720 A60 60 0 0 0 660 490 V570 H0 Z" fill="url(#paper)"/>
      <path class="web-pill-edge" d="M716 424 H1120 V556 H716 A66 66 0 0 1 716 424 Z" fill="var(--white)"/>
      <path class="web-pill" d="M718 432 H1120 V548 H718 A58 58 0 0 1 718 432 Z" fill="var(--green)"/>
    </svg>

    <div class="holder">
      <p class="holder-name">DANIEL HARTLEY</p>
      <p class="holder-role">Managing Director</p>
    </div>

    <ul class="contacts">
      <li class="address">
        <svg viewBox="0 0 24 24"><path d="M12 2a7 7 0 0 0-7 7c0 5.2 7 13 7 13s7-7.8 7-13a7 7 0 0 0-7-7zm0 9.5A2.5 2.5 0 1 1 12 6.5a2.5 2.5 0 0 1 0 5z"/></svg>
        <span>Level 18, 42 Harbour Street<br>Sydney</span>
      </li>
      <li>
        <svg viewBox="0 0 24 24"><path d="M6.6 10.8a15 15 0 0 0 6.6 6.6l2.2-2.2a1 1 0 0 1 1-.25 11.4 11.4 0 0 0 3.6.57 1 1 0 0 1 1 1V20a1 1 0 0 1-1 1A17 17 0 0 1 3 4a1 1 0 0 1 1-1h3.5a1 1 0 0 1 1 1c0 1.25.2 2.45.57 3.57a1 1 0 0 1-.25 1z"/></svg>
        <span>02 5550 1842</span>
      </li>
      <li>
        <svg viewBox="0 0 24 24"><path d="M6 2h9l3 3v5H6z M3 11h18v9H3z M7 14h4v2H7z"/></svg>
        <span>02 5550 1843</span>
      </li>
      <li>
        <svg viewBox="0 0 24 24"><path d="M2 5h20v14H2z M2 5l10 8 10-8" stroke="var(--white)" stroke-width="1.6"/></svg>
        <span>dhartley@rwl.com.au</span>
      </li>
    </ul>

    <p class="brand-name">RWL CAPITAL</p>
    <p class="website">www.rwlcapital.com.au</p>
  </div>
</body>
</html>
```